Business Card Design

We need a business card designed to portray the message that we are wedding and event stylists. We set up garden ceremonies and style wedding reception venues with chair covers and sashes, backdrops and draping's, wishing wells, tealight holders, table centerpieces. We also style corporate functions - Christmas parties, gala dinners, school formals, award nights. The colour of our uniforms are black and hot pink, if these colours could be incorporated. We would like to be able to use this design for letterhead, flyers and postcards etc. We would like the design to portray a professional, classic image that would relate to both spectrums of our business, weddings and corporate events. If you could develop a logo to incorporate would be great

Target Market(s)

brides, corporate compaines

Industry/Entity Type

Wedding

Contact Information for Business Card

Velvet Crest Occasions & Party Hire
Phone: 0417 553 916 Email:vcoph@fernmail.example
Web: www.velvetcrestoccasions.example.au

Requirements
Must have
• Must include that we set up for weddings, engagements, birthdays, anniversaries, corporate functions, school formals, any occasion.

```html
<!DOCTYPE html>
<html lang="en">
<head>
<meta charset="utf-8">
<title>Velvet Crest Occasions &amp; Party Hire — Business Card</title>
<link rel="stylesheet" href="https://fonts.googleapis.com/css2?family=Great+Vibes&family=Cinzel:wght@600;700&display=swap">
<style>
  :root {
    --card-black: #000000;
    --ink-white: #ffffff;
    --hot-pink: #f01ee0;
    --ghost-grey: #1e1e1e;
    --wash-lilac: #c38cf0;
    --wash-magenta: #f23cc2;
    --wash-coral: #f0504a;
    --wash-amber: #f0783c;
  }
  html, body {
    margin: 0;
    padding: 0;
    width: 1200px;
    height: 741px;
    overflow: hidden;
    background: var(--card-black);
  }
  .card {
    position: relative;
    width: 1200px;
    height: 741px;
    background: var(--card-black);
    overflow: hidden;
  }
  .hero {
    position: absolute;
    left: 0;
    top: 0;
    width: 1200px;
    height: 370px;
    background:
      radial-gradient(ellipse at 18% 30%, rgba(220,190,255,0.85) 0%, rgba(220,190,255,0) 45%),
      radial-gradient(ellipse at 85% 70%, rgba(240,120,60,0.8) 0%, rgba(240,120,60,0) 50%),
      linear-gradient(90deg, var(--wash-lilac) 0%, var(--wash-magenta) 42%, var(--wash-coral) 72%, var(--wash-amber) 100%);
  }
  .brand-name {
    position: absolute;
    left: 0;
    top: 0;
    width: 1200px;
    height: 370px;
    margin: 0;
    font-family: "Great Vibes", cursive;
    font-weight: 400;
    color: var(--ink-white);
  }
  .brand-name span {
    position: absolute;
    white-space: nowrap;
    line-height: 1;
  }
  .brand-line-one { left: 150px; top: 52px; font-size: 118px; }
  .brand-amp { left: 555px; top: 155px; font-size: 72px; }
  .brand-line-two { left: 340px; top: 198px; font-size: 118px; }
  .services {
    position: absolute;
    left: 0;
    top: 470px;
    width: 1200px;
    margin: 0;
    padding: 0;
    list-style: none;
    text-align: center;
    font-family: "Cinzel", serif;
    font-weight: 600;
    font-size: 25px;
    letter-spacing: 2px;
    color: var(--ghost-grey);
  }
  .services li { height: 49px; line-height: 49px; }
  .contact {
    position: absolute;
    left: 0;
    top: 494px;
    width: 1200px;
    text-align: center;
    font-family: "Cinzel", serif;
    font-weight: 700;
    color: var(--ink-white);
  }
  .contact p { margin: 0; white-space: nowrap; }
  .stylist { font-size: 26px; letter-spacing: 2px; height: 48px; line-height: 34px; }
  .details { font-size: 23px; letter-spacing: 2.5px; height: 50px; line-height: 34px; }
  .details .phone-number { color: var(--hot-pink); }
  .web { font-size: 23px; letter-spacing: 3px; line-height: 34px; }
</style>
</head>
<body>
  <main class="card">
    <div class="hero" role="img" aria-label="Soft abstract wash of lilac, hot pink and coral"></div>
    <h1 class="brand-name" aria-label="Velvet Crest Occasions &amp; Party Hire">
      <span class="brand-line-one">Velvet Crest Occasions</span>
      <span class="brand-amp">&amp;</span>
      <span class="brand-line-two">Party Hire</span>
    </h1>

    <ul class="services">
      <li>Styling for weddings | engagements</li>
      <li>Birthdays | anniversaries</li>
      <li>Corporate functions | school formals | any occasion</li>
    </ul>

    <section class="contact">
      <p class="stylist">SIENNA HARLOW | STYLIST</p>
      <p class="details">PHONE: <span class="phone-number">0417 553 916</span> | EMAIL: VCOPH@FERNMAIL.EXAMPLE</p>
      <p class="web">WWW.VELVETCRESTOCCASIONS.EXAMPLE.AU</p>
    </section>
  </main>
</body>
</html>
```